Velmor Glazing

Modern glazing company specializing in commercial fit outs, pool fencing, frameless showers and glass splash backs, im after a very young/modern logo, it doesnt have to be revelent to glazing and a classy "boss like" design for the card. thank you in advanced

im thinking carbon fiber back ground or something along that line with bright orange wording or something maybe, open to suggestions 

Fencing

company name, name, phone and products

```html
<!DOCTYPE html>
<html lang="en">
<head>
<meta charset="utf-8">
<title>Velmor Glazing – Business Card</title>
<link href="https://fonts.googleapis.com/css2?family=Ubuntu:wght@400;500&display=swap" rel="stylesheet">
<style>
  :root {
    --backdrop-top: #dcdcdc;
    --backdrop-bottom: #f2f2f2;
    --card-black: #141414;
    --card-charcoal: #262626;
    --accent-cyan: #6dcbdc;
    --text-light: #f0f0f0;
    --text-dark: #2a2a2a;
    --column-light: #cfcfcf;
    --column-mid: #7a7a7a;
    --column-dark: #2b2b2b;
  }
  * { box-sizing: border-box; margin: 0; padding: 0; }
  html, body { width: 1200px; height: 1000px; overflow: hidden; }
  body {
    position: relative;
    background: linear-gradient(to bottom, var(--backdrop-top) 0%, var(--backdrop-bottom) 30%, var(--backdrop-bottom) 100%);
    font-family: "Ubuntu", sans-serif;
  }
  .card {
    position: absolute;
    top: 220px;
    width: 540px;
    height: 333px;
    overflow: hidden;
    background: radial-gradient(ellipse at 70% 40%, var(--card-charcoal) 0%, var(--card-black) 75%);
  }
  .card--front { left: 43px; }
  .card--back { left: 616px; }

  .brand-column {
    position: absolute;
    top: 0;
    height: 100%;
    background: linear-gradient(to right, var(--column-dark), var(--column-mid) 50%, var(--column-light));
  }
  .card--front .brand-column { left: 199px; width: 137px; opacity: 0.55; }
  .card--back .brand-column { left: 49px; width: 107px; opacity: 0.8; }

  .wordmark {
    position: absolute;
    display: flex;
    align-items: center;
    gap: 7px;
    padding: 6px 4px;
    background: var(--card-black);
    color: var(--accent-cyan);
    font-weight: 500;
    letter-spacing: 2px;
    line-height: 1.05;
    text-transform: uppercase;
  }
  .wordmark__square {
    width: 10px; height: 10px;
    background: var(--accent-cyan);
    flex: none;
  }
  .card--front .wordmark { left: 196px; top: 200px; font-size: 20px; }
  .card--back .wordmark { left: 45px; top: 242px; font-size: 16px; }

  .contact {
    position: absolute;
    left: 209px;
    top: 66px;
    color: var(--text-light);
  }
  .contact__name {
    color: var(--accent-cyan);
    font-size: 26px;
    font-weight: 400;
    letter-spacing: 2.5px;
    text-transform: uppercase;
    margin-bottom: 18px;
  }
  .contact__row {
    display: flex;
    align-items: center;
    gap: 8px;
    font-size: 14px;
    letter-spacing: 0.8px;
    height: 30px;
  }
  .contact__row svg { width: 12px; height: 12px; fill: var(--text-light); flex: none; }

  .services__title {
    position: absolute;
    left: 209px;
    top: 222px;
    color: var(--text-light);
    font-size: 14px;
    letter-spacing: 1.2px;
    text-transform: uppercase;
  }
  .services__band {
    position: absolute;
    left: 205px;
    top: 244px;
    width: 340px;
    height: 52px;
    background: var(--accent-cyan);
    border-radius: 6px 0 0 6px;
    display: grid;
    grid-template-columns: 157px 1fr;
    align-content: center;
    row-gap: 6px;
    padding-left: 6px;
    color: var(--text-dark);
    font-size: 12.5px;
    letter-spacing: 0.3px;
    text-transform: uppercase;
    list-style: none;
  }
</style>
</head>
<body>

<section class="card card--front" aria-label="Card front">
  <div class="brand-column" role="img" aria-label="Vertical band of grey glass tiles"></div>
  <div class="wordmark"><span class="wordmark__square"></span>Velmor<br>Glazing</div>
</section>

<section class="card card--back" aria-label="Card back">
  <div class="brand-column" role="img" aria-label="Vertical band of grey glass tiles"></div>
  <div class="wordmark"><span class="wordmark__square"></span>Velmor<br>Glazing</div>

  <div class="contact">
    <h1 class="contact__name">Dane Corley</h1>
    <p class="contact__row">
      <svg viewBox="0 0 12 12" aria-hidden="true"><path d="M3 0h6a1 1 0 0 1 1 1v10a1 1 0 0 1-1 1H3a1 1 0 0 1-1-1V1a1 1 0 0 1 1-1zm.5 1.5v7.5h5V1.5z"/></svg>
      0400 555 218
    </p>
    <p class="contact__row">
      <svg viewBox="0 0 12 12" aria-hidden="true"><path d="M0 2.5h12v7H0z M0 2.5l6 4 6-4" stroke="#141414" stroke-width="0.8"/></svg>
      dane@velmorglazing.com
    </p>
    <p class="contact__row">
      <svg viewBox="0 0 12 12" aria-hidden="true"><circle cx="6" cy="6" r="6"/><path d="M6 0v12M0 6h12M2 2.5c2.5 1.5 5.5 1.5 8 0M2 9.5c2.5-1.5 5.5-1.5 8 0" stroke="#141414" stroke-width="0.8" fill="none"/></svg>
      www.velmorglazing.com
    </p>
  </div>

  <h2 class="services__title">Specializing in</h2>
  <ul class="services__band">
    <li>Commercial fit outs</li>
    <li>Frameless showers</li>
    <li>Pool fencing</li>
    <li>Glass splash backs</li>
  </ul>
</section>

</body>
</html>
```